Web design for small empirical brand consulting company that will sell a web-based brand tool

We need a totally new and very appealing website:
Purpose: We want to attract lots of potential customers with this website... especially, we want to sell our web-based tool markvista®... we want to be perceived as innovative, trendy, but solid and reliable… we want customers go to the website, login at „markvista®“ (see structure), and perceive how it works.. and the contacting us or in the near future being able to buy a login and work with the tool… so we want to a) inform (on the website or send the url to customers) and b) to „force“ potential customers getting in contact with us…
Structure (e.g.): Must Home, markvista®, About us, Contact (incl. legal notice); we are open for more, Nice to have e.g. references/clients, press... for example, we publish a nice book in a couple of months and might want to show it somewhere on the website as well...)
Layout: We would like to have more/mainly figures - may be animated or something like that – in specific those on slides 7 and 8 as well as 6 and 9 (which would be for our web-based tool markvista®...)... excellent, but simple and with few text…
Fonts: Eurostile; CMYK 100/23/100/19, CMYK 0/0/0/70
Logo: Would you please use the trelloway-logo used in this file?
Social Media: we think that it might make sense to be connected to facebook, twitter and so on as well…
Phantasy: May be it is possible to have something between a classic marketing research and an e-commerce website... just a thought... because it is mainly about the new tool that will be assessable through a login... but customers might want to contact us or vice versa in order to check how the tool will work (btw: you do not have further info about markvista® here... I know)… I dream of having a site where people go to and by components of our tool like at zorvik… click and buy and go for it…
It is possible to program it in php or java? Thanks.
Pages I personally like: Don’t know if that helps, but I personally like those websites just they seem so simple: http:// www.pelvarion.com/, http://www.quintabel.net/... but I am veeery open
Pages I do not like anymore: my own www.trelloway.ch

```html
<!DOCTYPE html>
<html lang="en">
<head>
<meta charset="utf-8">
<title>trelloway – brand measuring</title>
<link href="https://fonts.googleapis.com/css2?family=Ubuntu:wght@300;400;500;700&display=swap" rel="stylesheet">
<style>
:root{
  --green:#1d9f5c;
  --green-dark:#137a45;
  --green-light:#2bb673;
  --grey-text:#4d4d4d;
  --grey-soft:#8c8c8c;
  --line:#e3e3e3;
  --panel:#f3f3f3;
  --stage:#3a3e44;
  --btn:#4a4f57;
  --white:#ffffff;
  --orange:#f39a1e;
}
*{box-sizing:border-box;margin:0;padding:0}
html,body{width:1200px;height:2904px;overflow:hidden}
body{background:var(--stage);font-family:'Ubuntu',sans-serif;color:var(--grey-text)}
.page{position:absolute;left:120px;top:40px;width:960px;height:2820px;background:var(--white);overflow:hidden;box-shadow:0 10px 40px rgba(0,0,0,.45)}
.abs{position:absolute}

/* header */
.site-header{left:0;top:0;width:960px;height:88px;background:var(--white);border-bottom:1px solid var(--line)}
.brand{left:40px;top:24px;font-size:32px;font-weight:500;color:var(--grey-text);line-height:40px}
.nav{right:36px;top:32px;display:flex;gap:0}
.nav a{display:block;padding:0 28px;font-size:17px;color:var(--grey-text);text-decoration:none;border-left:1px solid var(--line)}
.nav a:first-child{border-left:none}
.nav a.active{color:var(--green);font-weight:500}

/* hero */
.hero{left:0;top:88px;width:960px;height:432px;background:radial-gradient(ellipse at 40% 55%,#c9d3dc 0%,#8fa0b1 45%,#56677a 100%)}
.hero-title{left:0;top:120px;width:960px;text-align:center;color:var(--white);font-size:40px;font-weight:700;line-height:48px;text-shadow:0 2px 6px rgba(0,0,0,.35)}
.btn{display:inline-block;background:var(--btn);color:var(--white);font-size:14px;padding:9px 18px;border-radius:3px}
.hero .btn{position:absolute;left:418px;top:240px;font-size:16px;padding:10px 22px}

/* partners */
.partners{left:0;top:520px;width:960px;height:120px;background:var(--white);border-bottom:1px solid var(--line)}
.partner{top:34px;height:52px;background:#e6e9ec;border-radius:4px}
.arrow{top:42px}

/* section titles */
.section-title{left:0;width:960px;text-align:center;font-size:42px;font-weight:300;color:var(--grey-text)}
.rule{height:1px;background:var(--line)}

/* forsters */
.forsters{left:0;top:640px;width:960px;height:440px;background:var(--white)}
.card{top:120px;width:180px;text-align:center}
.card svg{display:block;margin:0 auto 14px}
.card h3{font-size:16px;font-weight:500;color:var(--grey-text);margin-bottom:8px}
.card p{font-size:13px;color:var(--grey-soft);line-height:18px;margin-bottom:16px;height:36px}

/* benefits */
.benefits{left:0;top:1080px;width:960px;height:520px;background:var(--panel)}
.benefit{top:150px;width:180px;text-align:center}
.benefit .disc{width:112px;height:112px;border-radius:50%;background:var(--green);margin:0 auto 20px;display:flex;align-items:center;justify-content:center}
.benefit h3{font-size:16px;font-weight:500;margin-bottom:8px}
.benefit p{font-size:13px;color:var(--grey-soft);line-height:18px}

/* about */
.about{left:0;top:1600px;width:960px;height:340px;background:linear-gradient(135deg,var(--green-light),var(--green) 55%,var(--green-dark))}
.about h2{font-size:38px;font-weight:400;color:var(--white)}
.about p{font-size:14px;line-height:21px;color:#dff3e8}
.btn-dark{background:#1a5c3a}
.member{left:470px;width:440px;height:80px;background:rgba(255,255,255,.12);border-radius:4px}
.avatar{left:14px;top:10px;width:60px;height:60px;border-radius:50%;background:linear-gradient(#c9a890,#8d6f5d);border:3px solid rgba(255,255,255,.7)}
.member h4{position:absolute;left:92px;top:18px;font-size:15px;font-weight:500;color:var(--white)}
.member span{position:absolute;left:92px;top:42px;font-size:12px;color:#cfeedd}

/* testimonial */
.testimonial{left:0;top:1940px;width:960px;height:400px;background:var(--white)}
.quote-mark{font-size:150px;color:#d7ede1;font-weight:700;line-height:1}
.testimonial p{left:280px;top:160px;width:400px;text-align:center;font-size:16px;line-height:25px;color:var(--grey-soft)}
.cite{left:0;top:250px;width:960px;text-align:center;color:var(--green);font-size:15px}
.dots{left:0;top:320px;width:960px;display:flex;justify-content:center;gap:12px}
.dots i{width:14px;height:14px;border-radius:50%;background:var(--btn)}
.dots i.on{background:var(--green)}

/* contact */
.contact{left:0;top:2340px;width:960px;height:390px}
.map{position:absolute;inset:0;background:linear-gradient(120deg,#a9d6ad 0%,#c7e3c3 40%,#d9e7d8 60%,#7fb6d1 100%)}
.contact-box{left:150px;top:80px;width:300px;height:230px;background:var(--white);border-radius:4px;box-shadow:0 4px 14px rgba(0,0,0,.15);padding:22px 26px}
.contact-box h2{font-size:26px;font-weight:400;color:var(--green);margin-bottom:18px}
.contact-line{display:flex;align-items:center;gap:12px;font-size:14px;color:var(--grey-text);margin-bottom:16px}

/* footer */
.site-footer{left:0;top:2730px;width:960px;height:90px;background:var(--white);border-top:1px solid var(--line)}
.site-footer .brand{top:25px;font-size:28px}
.socials{left:412px;top:30px;display:flex;gap:10px}
.socials i{width:30px;height:30px;border-radius:50%;background:var(--green)}
.copyright{right:40px;top:36px;font-size:13px;color:var(--grey-soft)}
.copyright b{color:var(--green);font-weight:500}
</style>
</head>
<body>
<div class="page">

  <header class="site-header abs">
    <div class="brand abs">trelloway</div>
    <nav class="nav abs">
      <a class="active">Home</a><a>markvista®</a><a>About us</a><a>Contact us</a>
    </nav>
  </header>

  <section class="hero abs" role="img" aria-label="Businessman touching a glowing network of lines over a world map">
    <h1 class="hero-title abs">Simply measuring and modeling<br>your brand success</h1>
    <span class="btn">Read More »</span>
  </section>

  <section class="partners abs">
    <svg class="arrow abs" style="left:24px" width="20" height="36" viewBox="0 0 20 36"><path d="M16 4 L4 18 L16 32" fill="none" stroke="#9a9a9a" stroke-width="3"/></svg>
    <div class="partner abs" style="left:120px;width:130px"></div>
    <div class="partner abs" style="left:320px;width:150px"></div>
    <div class="partner abs" style="left:540px;width:140px;background:#f4dc3c"></div>
    <div class="partner abs" style="left:750px;width:90px"></div>
    <svg class="arrow abs" style="left:916px" width="20" height="36" viewBox="0 0 20 36"><path d="M4 4 L16 18 L4 32" fill="none" stroke="#9a9a9a" stroke-width="3"/></svg>
  </section>

  <section class="forsters abs">
    <div class="rule abs" style="left:120px;top:60px;width:200px"></div>
    <h2 class="section-title abs" style="top:32px">Our Forsters</h2>
    <div class="rule abs" style="left:640px;top:60px;width:200px"></div>

    <div class="card abs" style="left:60px">
      <svg width="90" height="90" viewBox="0 0 90 90"><path d="M10 48 L28 30 L44 36 L60 28 L80 46 L60 64 L48 70 L30 58 Z" fill="var(--green)"/><path d="M32 46 L44 56 M40 42 L52 52" stroke="#fff" stroke-width="3"/></svg>
      <h3>Closeness</h3>
      <p>Close ties with every client we serve.</p>
      <span class="btn">Read More »</span>
    </div>
    <div class="card abs" style="left:280px">
      <svg width="90" height="90" viewBox="0 0 90 90"><path d="M45 10 L76 20 L74 48 Q70 70 45 82 Q20 70 16 48 L14 20 Z" fill="none" stroke="var(--green)" stroke-width="6"/><path d="M32 46 L42 56 L60 36" fill="none" stroke="var(--green)" stroke-width="7"/></svg>
      <h3>Security</h3>
      <p>Solid data you can always rely on.</p>
      <span class="btn">Read More »</span>
    </div>
    <div class="card abs" style="left:500px">
      <svg width="90" height="90" viewBox="0 0 90 90"><circle cx="45" cy="45" r="34" fill="var(--green)"/><path d="M45 22 L45 68 M22 45 L68 45" stroke="#fff" stroke-width="6"/><circle cx="45" cy="45" r="9" fill="#fff"/></svg>
      <h3>Fit</h3>
      <p>Tools that fit your brand and goals.</p>
      <span class="btn">Read More »</span>
    </div>
    <div class="card abs" style="left:720px">
      <svg width="90" height="90" viewBox="0 0 90 90"><circle cx="38" cy="30" r="14" fill="var(--green)"/><path d="M12 74 Q14 48 38 48 Q62 48 64 74 Z" fill="var(--green)"/><circle cx="66" cy="58" r="14" fill="#fff" stroke="var(--green)" stroke-width="4"/><path d="M59 58 L65 64 L74 52" fill="none" stroke="var(--green)" stroke-width="4"/></svg>
      <h3>Customer loyalty</h3>
      <p>Lasting bonds built on clear results.</p>
      <span class="btn">Read More »</span>
    </div>
  </section>

  <section class="benefits abs">
    <div class="rule abs" style="left:120px;top:80px;width:220px;background:#d8d8d8"></div>
    <h2 class="section-title abs" style="top:52px">Our Benefits</h2>
    <div class="rule abs" style="left:620px;top:80px;width:220px;background:#d8d8d8"></div>

    <div class="benefit abs" style="left:60px">
      <div class="disc"><svg width="56" height="56" viewBox="0 0 56 56"><rect x="6" y="32" width="10" height="18" fill="#fff"/><rect x="22" y="20" width="10" height="30" fill="#fff"/><rect x="38" y="8" width="10" height="42" fill="#fff"/></svg></div>
      <h3>Metrics</h3>
      <p>Clear figures show how your brand is seen in the market.</p>
    </div>
    <div class="benefit abs" style="left:280px">
      <div class="disc"><svg width="60" height="56" viewBox="0 0 60 56"><rect x="22" y="4" width="16" height="12" fill="#fff"/><rect x="4" y="38" width="16" height="12" fill="#fff"/><rect x="22" y="38" width="16" height="12" fill="#fff"/><rect x="40" y="38" width="16" height="12" fill="#fff"/><path d="M30 16 V28 M12 38 V28 H48 V38 M30 28 V38" fill="none" stroke="#fff" stroke-width="3"/></svg></div>
      <h3>Trend models</h3>
      <p>Models reveal where your brand is heading next year.</p>
    </div>
    <div class="benefit abs" style="left:500px">
      <div class="disc"><svg width="56" height="56" viewBox="0 0 56 56"><circle cx="28" cy="18" r="12" fill="#fff"/><path d="M6 54 Q8 32 28 32 Q48 32 50 54 Z" fill="#fff"/></svg></div>
      <h3>Precision</h3>
      <p>Exact insight into each target group you want to reach.</p>
    </div>
    <div class="benefit abs" style="left:720px">
      <div class="disc"><svg width="56" height="56" viewBox="0 0 56 56"><circle cx="28" cy="28" r="22" fill="#fff"/><text x="28" y="38" text-anchor="middle" font-family="Ubuntu, sans-serif" font-size="28" font-weight="700" fill="var(--green)">$</text></svg></div>
      <h3>Cost reduction</h3>
      <p>Focused spending cuts waste across all your campaigns.</p>
    </div>
  </section>

  <section class="about abs">
    <h2 class="abs" style="left:50px;top:36px">About us</h2>
    <p class="abs" style="left:50px;top:100px;width:360px">We are a small empirical brand consulting team. We turn survey data into clear models that show how strong your brand really is and where it can grow.</p>
    <span class="btn btn-dark abs" style="left:50px;top:240px;font-size:15px">Read More »</span>

    <h2 class="abs" style="left:470px;top:36px;font-size:34px">The main team</h2>
    <div class="member abs" style="top:108px">
      <div class="avatar abs" role="img" aria-label="Portrait of Lukas Berner"></div>
      <h4>Lukas Berner, Dr.</h4>
      <span>Founder and head of brand modeling</span>
    </div>
    <div class="member abs" style="top:212px">
      <div class="avatar abs" role="img" aria-label="Portrait of Jonas Kessler"></div>
      <h4>Jonas Kessler, Dr. oec.</h4>
      <span>Partner, research and data analysis</span>
    </div>
  </section>

  <section class="testimonial abs">
    <h2 class="section-title abs" style="top:30px;font-size:52px">What customers are saying:</h2>
    <span class="quote-mark abs" style="left:200px;top:100px">“</span>
    <p class="abs">I loved my book. The quality was amazing and the layout was beautiful. Ordering was easy and it Shipped quicker than expected.</p>
    <span class="quote-mark abs" style="left:700px;top:170px">”</span>
    <div class="cite abs">- Customer Name</div>
    <div class="dots abs"><i class="on"></i><i></i><i></i><i></i></div>
  </section>

  <section class="contact abs">
    <div class="map" role="img" aria-label="Street map of the office surroundings"></div>
    <svg class="abs" style="left:520px;top:110px" width="220" height="220" viewBox="0 0 220 220"><circle cx="110" cy="110" r="100" fill="rgba(255,255,255,.35)"/><circle cx="110" cy="110" r="56" fill="rgba(255,255,255,.45)"/><path d="M110 40 C90 40 78 56 78 72 C78 96 110 128 110 128 C110 128 142 96 142 72 C142 56 130 40 110 40 Z" fill="var(--orange)"/><circle cx="110" cy="72" r="12" fill="#fff"/></svg>
    <div class="contact-box abs">
      <h2>Contact US</h2>
      <div class="contact-line"><svg width="18" height="18" viewBox="0 0 18 18"><path d="M4 1 L7 5 L5 7 Q7 11 11 13 L13 11 L17 14 L15 17 Q4 16 1 3 Z" fill="var(--green)"/></svg>+41 44 555 01 72</div>
      <div class="contact-line"><svg width="18" height="14" viewBox="0 0 18 14"><rect x="1" y="1" width="16" height="12" fill="none" stroke="var(--green)" stroke-width="2"/><path d="M1 1 L9 8 L17 1" fill="none" stroke="var(--green)" stroke-width="2"/></svg>l.berner@trelloway.ch</div>
      <div class="contact-line"><svg width="16" height="20" viewBox="0 0 16 20"><path d="M8 1 C4 1 1 4 1 8 C1 13 8 19 8 19 C8 19 15 13 15 8 C15 4 12 1 8 1 Z" fill="var(--green)"/><circle cx="8" cy="8" r="3" fill="#fff"/></svg>Lindenhofweg 14</div>
    </div>
  </section>

  <footer class="site-footer abs">
    <div class="brand abs">trelloway</div>
    <div class="socials abs"><i></i><i></i><i></i><i></i></div>
    <div class="copyright abs"><b>@trelloway</b> All rights reserved 2013</div>
  </footer>

</div>
</body>
</html>
```